Design a website for a quickly growing ghostwriting and editing firm

NRF Productions has a website through Wix, but we need help! We are based in Austin, TX, and we work primarily with self-help, wellness, and diet authors. We offer ghostwriting, editing and book development services. You can see our basic site now at www.nadiafernproductions.com

```html
<!DOCTYPE html>
<html lang="en">
<head>
<meta charset="utf-8">
<title>NRF Productions – Ghostwriting &amp; Editing</title>
<link href="https://fonts.googleapis.com/css2?family=Poppins:wght@300;400;500;600;700&display=swap" rel="stylesheet">
<style>
:root{
  --peach:#f5b594;
  --terracotta:#d98b6f;
  --ink:#0c0c0c;
  --dark:#111111;
  --text:#555555;
  --offwhite:#f9f8f5;
  --white:#ffffff;
  --hero-a:#2c3a4a;
  --hero-b:#6b5d52;
}
*{margin:0;padding:0;box-sizing:border-box}
html,body{width:1200px;height:3553px;overflow:hidden}
body{position:relative;font-family:'Poppins',sans-serif;background:var(--white);color:var(--ink)}
/* hero */
.hero{position:absolute;left:0;top:0;width:1200px;height:680px;background:linear-gradient(120deg,var(--hero-a) 0%,#3f4b56 45%,var(--hero-b) 100%)}
.hero-photo{position:absolute;inset:0;background:radial-gradient(ellipse at 70% 60%,rgba(180,160,140,.35),transparent 60%),linear-gradient(180deg,rgba(10,20,30,.35),rgba(10,20,30,.55))}
.brand{position:absolute;display:flex;align-items:center;gap:12px;color:var(--white);font-weight:300;font-size:26px;letter-spacing:.5px}
.brand-dot{width:52px;height:52px;border-radius:50%;background:var(--terracotta)}
.hero .brand{left:92px;top:38px}
.nav{position:absolute;top:55px;left:518px;display:flex;list-style:none}
.nav li{font-size:11.5px;color:var(--white);font-weight:500;padding:6px 12px;margin-right:14px;border-radius:16px}
.nav li.active{background:var(--peach)}
.social-top{position:absolute;top:60px;left:992px;display:flex;gap:22px}
.social-top span{width:12px;height:12px;border-radius:50%;background:var(--white);opacity:.9}
.hero-title{position:absolute;top:212px;left:0;width:1200px;text-align:center;color:var(--white);font-weight:700;font-size:74px;letter-spacing:-.5px}
.hero-title .amp{font-weight:300}
.hero-lead{position:absolute;top:326px;left:220px;width:760px;text-align:center;color:var(--white);font-weight:300;font-size:21.5px;line-height:34px}
.dots{position:absolute;top:452px;left:562px;display:flex;gap:16px}
.dots span{width:15px;height:15px;border-radius:50%;border:2px solid var(--white)}
.dots span.on{background:var(--white)}
.wave{position:absolute;left:0}
/* about */
.about-photo{position:absolute;left:115px;top:714px;width:510px;height:510px;border-radius:50%;background:radial-gradient(circle at 60% 40%,#cfcfd2,#8f8f95 55%,#2b2b2e 100%)}
.about-ring{position:absolute;left:137px;top:730px;width:468px;height:468px;border-radius:50%;border:2px solid var(--white)}
.about{position:absolute;left:700px;top:818px;width:350px;text-align:center}
.about h2{font-size:41px;font-weight:700;line-height:1.1}
.about .sub{font-size:12px;font-weight:500;margin-top:14px}
.about p{font-size:12.5px;line-height:20.5px;color:var(--text);margin-top:38px;font-weight:300}
.btn{display:inline-block;background:var(--peach);color:var(--white);font-size:12px;font-weight:500;border-radius:20px}
.about .btn{margin-top:26px;width:95px;height:36px;line-height:36px}
/* stats */
.stats{position:absolute;left:0;top:1316px;width:1200px;height:238px;background:linear-gradient(100deg,#d68e74,#df9a7d 50%,#d3876c)}
.stat{position:absolute;top:54px;width:200px;text-align:center;color:var(--white)}
.stat b{display:block;font-size:62px;font-weight:600;line-height:1.1}
.stat i{display:block;width:26px;height:2px;background:var(--white);margin:6px auto 22px}
.stat em{font-style:normal;font-size:12px;font-weight:500}
/* offer */
.section-title{position:absolute;left:0;width:1200px;text-align:center;font-weight:700;font-size:41px}
.offer{position:absolute;top:1768px;width:280px;text-align:center}
.offer-icon{width:128px;height:128px;border-radius:50%;border:2px solid var(--ink);margin:0 auto;display:flex;align-items:center;justify-content:center}
.offer-icon .core{width:112px;height:112px;border-radius:50%;background:var(--ink);display:flex;align-items:center;justify-content:center}
.offer-icon.alt .core{background:var(--peach)}
.offer h3{font-size:21px;font-weight:500;margin-top:22px}
.offer p{font-size:12px;line-height:20.5px;color:var(--text);margin-top:14px;font-weight:300}
/* blog */
.blog-bg{position:absolute;left:0;top:2260px;width:1200px;height:820px;background:var(--offwhite)}
.card{position:absolute;top:2451px;width:406px;height:497px;background:var(--white)}
.card-img{height:233px}
.card-meta{height:52px;background:var(--peach);color:var(--white);font-size:12px;font-weight:500;display:flex;align-items:center;gap:18px;padding-left:36px}
.card-meta span{display:flex;align-items:center;gap:6px}
.card h3{font-size:21.5px;font-weight:500;margin:30px 0 0 36px}
.card p{font-size:12px;line-height:20.5px;color:var(--text);margin:14px 30px 0 36px;font-weight:300}
.card a{display:block;font-size:12px;color:var(--peach);margin:14px 0 0 36px;text-decoration:none}
/* footer */
.footer{position:absolute;left:0;top:3079px;width:1200px;height:425px;background:var(--dark);color:var(--white)}
.footer .brand{left:179px;top:88px}
.contact-line{position:absolute;left:190px;display:flex;gap:20px;font-size:12px;line-height:20.5px;font-weight:300}
.contact-line svg{flex:none;margin-top:4px}
.contact-line span{display:block;width:200px}
.social-foot{position:absolute;left:195px;top:340px;display:flex;gap:6px}
.social-foot span{width:16px;height:16px;border-radius:50%;border:1.5px solid var(--white)}
.footer h4{position:absolute;top:94px;font-size:20px;font-weight:500}
.links{position:absolute;left:556px;top:157px;list-style:none;font-size:12px;line-height:20.7px}
.field{position:absolute;left:780px;width:258px;height:44px;border-radius:22px;background:var(--white);color:#b5b5b5;font-size:11px;padding-left:26px;line-height:44px}
.send{position:absolute;left:780px;top:269px;width:258px;height:44px;border-radius:22px;background:var(--peach);color:var(--ink);font-size:12px;font-weight:600;text-align:center;line-height:44px}
.copyright{position:absolute;left:0;top:3504px;width:1200px;height:49px;background:var(--peach);text-align:center;line-height:49px;font-size:12px}
</style>
</head>
<body>

<header class="hero">
  <div class="hero-photo" role="img" aria-label="Photo of a person writing in a notebook beside a laptop"></div>
  <div class="brand"><span class="brand-dot"></span>NRF Productions</div>
  <ul class="nav">
    <li class="active">HOME</li><li>ABOUT ME</li><li>WORKSHOPS</li><li>BLOG</li><li>CONTACT</li>
  </ul>
  <div class="social-top" aria-label="Social links"><span></span><span></span><span></span></div>
  <h1 class="hero-title">Ghostwriting <span class="amp">&amp;</span> Editing</h1>
  <p class="hero-lead">Maecenas vel auctor odio. Praesent vitae placerat arcu. Ut sit amet dolor at turpis vulputate sagittis. In accumsan libero a ultrices</p>
  <div class="dots"><span class="on"></span><span></span><span></span></div>
</header>
<svg class="wave" style="top:500px" width="1200" height="190" viewBox="0 0 1200 190">
  <path d="M0 18 C150 70 330 40 520 60 C700 80 780 165 900 170 C1010 175 1060 60 1200 55 L1200 190 L0 190Z" fill="var(--peach)"/>
  <path d="M0 32 C150 80 330 62 520 82 C700 100 780 150 900 150 C1010 150 1060 80 1200 78 L1200 190 L0 190Z" fill="var(--white)"/>
</svg>

<section>
  <div class="about-photo" role="img" aria-label="Photo of a woman writing notes at her laptop"></div>
  <div class="about-ring"></div>
  <div class="about">
    <h2>About Us</h2>
    <div class="sub">Ghostwriting and Editing</div>
    <p>Maecenas vel auctor odio. Praesent vitae placerat arcu. Ut sit amet dolor at turpis vulputate sagittis. In accumsan libero a ultrices imperdiet. Nam commodo felis libero, ac lacinia nulla aliquet sed. Fusce vel fermentum diam, id accumsan sapien. Vestibulum a lacinia massa, tempor pulvinar urna. Pellentesque volutpat diam ac magna.</p>
    <span class="btn">View More</span>
  </div>
</section>

<section class="stats">
  <div class="stat" style="left:145px"><b>20</b><i></i><em>Years Experience</em></div>
  <div class="stat" style="left:398px"><b>980</b><i></i><em>People Across</em></div>
  <div class="stat" style="left:660px"><b>120</b><i></i><em>Writen Books</em></div>
  <div class="stat" style="left:900px"><b>20</b><i></i><em>Self Articles</em></div>
</section>

<section>
  <h2 class="section-title" style="top:1668px">What We Offer</h2>
  <div class="offer" style="left:103px">
    <div class="offer-icon"><div class="core">
      <svg width="64" height="64" viewBox="0 0 64 64" fill="none" stroke="#fff" stroke-width="2.5"><rect x="8" y="10" width="48" height="34" rx="2"/><path d="M24 54h16M32 44v10M16 20h20M16 27h16M16 34h12M48 18l-10 14-3 5 5-3 10-14z"/></svg>
    </div></div>
    <h3>Ghostwriting</h3>
    <p>Maecenas vel auctor odio. Praesent vitae placerat arcu. Ut sit amet dolor at turpis vulputate sagittis. In accu</p>
  </div>
  <div class="offer" style="left:459px">
    <div class="offer-icon alt"><div class="core">
      <svg width="64" height="64" viewBox="0 0 64 64" fill="none" stroke="var(--ink)" stroke-width="2.5"><path d="M8 14h20a4 4 0 0 1 4 4v32a4 4 0 0 0-4-4H8zM56 14H36a4 4 0 0 0-4 4v32a4 4 0 0 1 4-4h20z"/><path d="M14 22h10M14 29h10M14 36h10M40 22h6M40 29h6M50 18v22l-2 4-2-4V18z"/></svg>
    </div></div>
    <h3>Editing</h3>
    <p>Maecenas vel auctor odio. Praesent vitae placerat arcu. Ut sit amet dolor at turpis vulputate sagittis. In accu</p>
  </div>
  <div class="offer" style="left:813px">
    <div class="offer-icon"><div class="core">
      <svg width="64" height="64" viewBox="0 0 64 64" fill="none" stroke="#fff" stroke-width="2.5"><path d="M18 44h-2a10 10 0 0 1 0-20 14 14 0 0 1 27-4 10 10 0 0 1 5 19"/><rect x="22" y="30" width="18" height="24" rx="2"/><path d="M26 36h10M26 41h10M26 46h6"/></svg>
    </div></div>
    <h3>Book development</h3>
    <p>Maecenas vel auctor odio. Praesent vitae placerat arcu. Ut sit amet dolor at turpis vulputate sagittis. In accu</p>
  </div>
</section>

<div class="blog-bg"></div>
<svg class="wave" style="top:2090px" width="1200" height="180" viewBox="0 0 1200 180">
  <path d="M0 42 C140 28 260 110 400 145 C520 172 640 112 800 82 C980 55 1100 38 1200 0 L1200 180 L0 180Z" fill="var(--peach)"/>
  <path d="M0 62 C140 50 260 122 400 158 C520 182 640 128 800 98 C980 72 1100 56 1200 20 L1200 180 L0 180Z" fill="var(--offwhite)"/>
</svg>

<section>
  <h2 class="section-title" style="top:2328px">Blog about current topics</h2>
  <article class="card" style="left:178px">
    <div class="card-img" role="img" aria-label="Photo of a man writing at his desk" style="background:linear-gradient(135deg,#d9d6cf,#8a8378 60%,#4b4740)"></div>
    <div class="card-meta"><span>
      <svg width="14" height="14" viewBox="0 0 16 16" fill="none" stroke="#fff" stroke-width="1.4"><circle cx="8" cy="8" r="7"/><circle cx="8" cy="6.5" r="2.5"/><path d="M3.5 13c1.5-2.5 7.5-2.5 9 0"/></svg>admin</span><span>
      <svg width="14" height="14" viewBox="0 0 16 16" fill="none" stroke="#fff" stroke-width="1.4"><rect x="1.5" y="3" width="13" height="11.5" rx="1"/><path d="M1.5 6.5h13M5 1v3M11 1v3"/></svg>08/03/2016</span></div>
    <h3>Vivamus porta orci eu</h3>
    <p>Maecenas vel auctor odio. Praesent vitae placerat arcu. Ut sit amet dolor at turpis vulputate sagittis. In accumsan libero a ultrices imperdiet.</p>
    <a>View More</a>
  </article>
  <article class="card" style="left:619px">
    <div class="card-img" role="img" aria-label="Photo of hands typing on a laptop keyboard" style="background:linear-gradient(135deg,#e8e6e2,#a9a6a1 55%,#6e6a66)"></div>
    <div class="card-meta"><span>
      <svg width="14" height="14" viewBox="0 0 16 16" fill="none" stroke="#fff" stroke-width="1.4"><circle cx="8" cy="8" r="7"/><circle cx="8" cy="6.5" r="2.5"/><path d="M3.5 13c1.5-2.5 7.5-2.5 9 0"/></svg>admin</span><span>
      <svg width="14" height="14" viewBox="0 0 16 16" fill="none" stroke="#fff" stroke-width="1.4"><rect x="1.5" y="3" width="13" height="11.5" rx="1"/><path d="M1.5 6.5h13M5 1v3M11 1v3"/></svg>08/03/2016</span></div>
    <h3>Vivamus porta orci eu</h3>
    <p>Maecenas vel auctor odio. Praesent vitae placerat arcu. Ut sit amet dolor at turpis vulputate sagittis. In accumsan libero a ultrices imperdiet.</p>
    <a>View More</a>
  </article>
</section>

<footer class="footer">
  <div class="brand"><span class="brand-dot"></span>NRF Productions</div>
  <div class="contact-line" style="top:186px">
    <svg width="14" height="14" viewBox="0 0 16 16" fill="#fff"><path d="M3 1l3 3-1.5 2a9 9 0 0 0 5.5 5.5L12 10l3 3-2 2C7 15 1 9 1 3z"/></svg><span>+00 512 870 246</span></div>
  <div class="contact-line" style="top:227px">
    <svg width="14" height="12" viewBox="0 0 16 12" fill="#fff"><path d="M0 0h16v12H0z M1 1l7 5 7-5" stroke="#111" stroke-width="1.2"/></svg><span>hello@nrfmail.com</span></div>
  <div class="contact-line" style="top:268px">
    <svg width="14" height="16" viewBox="0 0 14 18" fill="#fff"><path d="M7 0a7 7 0 0 0-7 7c0 5 7 11 7 11s7-6 7-11a7 7 0 0 0-7-7zm0 9.5A2.5 2.5 0 1 1 7 4.5a2.5 2.5 0 0 1 0 5z"/></svg><span>PO Box 41210 Cedar st. 220, Austin, Texas, US.</span></div>
  <div class="social-foot" aria-label="Social links"><span></span><span></span><span></span></div>
  <h4 style="left:556px">Links</h4>
  <ul class="links"><li>About me</li><li>FAQs</li><li>Contact</li><li>Clients</li><li>News</li><li>Success Stories</li><li>Shop</li><li>Privacy policy</li></ul>
  <h4 style="left:779px">Contact Us</h4>
  <div class="field" style="top:157px">Your Name...</div>
  <div class="field" style="top:214px">Your Email...</div>
  <div class="send">Send Message</div>
</footer>
<div class="copyright">Copyright © 2021 NRF Productions</div>

</body>
</html>
```